New Business Card Design Project

We require a business card design for Zelvaquin, a newly established Indian company.
Our focus is on the development, manufacturing, and export of a diverse array of pharmaceutical products on a global scale. The card should convey a professional appearance, as our primary markets are in Africa, China, and Southeast Asian nations.
We envision a two-sided business card, with the reverse side dedicated to a logo set against a solid color or an elegantly designed pattern. The corners should be rounded. We would appreciate seeing both horizontal and vertical design options. We trust the designer to utilize their expertise in creating this design.

The content for the business card is included in the attached Word file.

Target Market(s)

Our primary markets are in Africa, China, and Southeast Asian, Latin America, Maldives, Sri Lanka

Industry/Entity Type

Pharmaceutical Manufacturing and Export

Contact Information for Business Card

Colors

Designer to choose colors to be used in the design.

Requirements
Must have
• The reverse side of the business card features solely the logo along with the tagline, "Healing Every Day."
Should not have
• The logo should not exceed two instances, encompassing both the front and back sides of the card.

```html
<!DOCTYPE html>
<html lang="en">
<head>
<meta charset="utf-8">
<title>Zelvaquin Business Card</title>
<link href="https://fonts.googleapis.com/css2?family=Montserrat:wght@400;500;600;700&display=swap" rel="stylesheet">
<style>
  :root {
    --blue: #29a8e0;
    --red: #ef5a46;
    --ink: #555a60;
    --paper: #ffffff;
    --backdrop: #3a3a3c;
  }
  * { margin: 0; padding: 0; box-sizing: border-box; }
  html, body { width: 1200px; height: 987px; overflow: hidden; }
  body {
    background: var(--backdrop);
    font-family: "Montserrat", sans-serif;
    position: relative;
  }
  .card {
    position: absolute;
    width: 620px;
    height: 354px;
    background: var(--paper);
    border-radius: 10px;
    overflow: hidden;
    box-shadow: 0 14px 30px rgba(0,0,0,0.45);
  }
  .card--back { left: 90px; top: 90px; }
  .card--front { left: 490px; top: 520px; }

  /* reverse side */
  .back-brand {
    position: absolute;
    left: 0; right: 0; top: 88px;
    text-align: center;
  }
  .brand-mark {
    display: block;
    width: 46px; height: 46px;
    margin: 0 auto 18px;
    border-radius: 50%;
    background: var(--blue);
  }
  .brand-name {
    color: var(--blue);
    font-weight: 700;
    font-size: 52px;
    letter-spacing: 0.5px;
    line-height: 1;
  }
  .tagline {
    position: absolute;
    left: 0; right: 0; bottom: 48px;
    text-align: center;
    font-weight: 600;
    font-size: 16px;
    letter-spacing: 0.5px;
    color: var(--blue);
  }

  /* front side */
  .front-brand {
    position: absolute;
    left: 40px; top: 104px;
    width: 290px;
    text-align: center;
  }
  .front-brand .brand-name { font-size: 46px; }
  .divider {
    position: absolute;
    left: 340px; top: 58px;
    width: 2px; height: 196px;
    background: var(--red);
  }
  .contact {
    position: absolute;
    left: 366px; top: 56px;
    width: 240px;
    color: var(--ink);
  }
  .contact__name {
    color: var(--blue);
    font-weight: 600;
    font-size: 22px;
    letter-spacing: 0.3px;
    white-space: nowrap;
  }
  .contact__role {
    font-size: 15px;
    margin-top: 2px;
  }
  .contact__address {
    font-size: 14px;
    line-height: 1.35;
    margin-top: 18px;
  }
  .contact__list {
    list-style: none;
    margin-top: 16px;
    font-size: 14px;
    line-height: 1.5;
  }
  .contact__list li { display: flex; align-items: center; gap: 9px; white-space: nowrap; }
  .contact__list svg { width: 13px; height: 13px; flex: none; }
  .band { position: absolute; bottom: 0; left: 0; width: 620px; height: 18px; }
</style>
</head>
<body>

<section class="card card--back" aria-label="Card reverse side">
  <div class="back-brand">
    <span class="brand-mark"></span>
    <div class="brand-name">Zelvaquin</div>
  </div>
  <p class="tagline">Healing Every Day.</p>
</section>

<section class="card card--front" aria-label="Card front side">
  <div class="front-brand">
    <span class="brand-mark"></span>
    <div class="brand-name">Zelvaquin</div>
  </div>
  <div class="divider"></div>
  <div class="contact">
    <h1 class="contact__name">Arvind K. Solanke</h1>
    <p class="contact__role">CEO</p>
    <p class="contact__address">14, Gulmohar Nagar, Wardha<br>442001, India</p>
    <ul class="contact__list">
      <li>
        <svg viewBox="0 0 14 14" fill="none" stroke="#ef5a46" stroke-width="1.5"><rect x="3.5" y="1" width="7" height="12" rx="1.3"/><line x1="6" y1="11" x2="8" y2="11"/></svg>
        +919800012345
      </li>
      <li>
        <svg viewBox="0 0 14 14"><rect x="1" y="3" width="12" height="8.5" fill="#ef5a46"/><path d="M1 3 L7 8 L13 3" fill="none" stroke="#fff" stroke-width="1.2"/></svg>
        asolanke@zelvaquin.com
      </li>
      <li>
        <svg viewBox="0 0 14 14" fill="none" stroke="#ef5a46" stroke-width="1.2"><circle cx="7" cy="7" r="5.8"/><ellipse cx="7" cy="7" rx="2.5" ry="5.8"/><line x1="1.2" y1="7" x2="12.8" y2="7"/><line x1="2" y1="4" x2="12" y2="4"/><line x1="2" y1="10" x2="12" y2="10"/></svg>
        zelvaquin.com
      </li>
    </ul>
  </div>
  <svg class="band" viewBox="0 0 620 18" preserveAspectRatio="none">
    <polygon points="0,0 365,0 355,18 0,18" fill="#29a8e0"/>
    <polygon points="371,0 620,0 620,18 361,18" fill="#ef5a46"/>
  </svg>
</section>

</body>
</html>
```